Day Spa needs attracting information signage board

Need a sign that states our name, telephone number and web address. Have a logo but not imperitave to use. Sign needs to attract clients since it's on street without many pedestrians but many cars driving by.

Target Market(s)

Females aged 18 to 60 interested in health and beauty as well as slimming. Females that want to have days off and enjoy a full day at a spa. 10% Males

Requirements
Must have
• Name - Lesedi Day Spa
Tel - 011 742 3198 / 011 657 4031
Web address: www.lesedidayspa.example.za
Address: 23 Kestrel road (with a sign showing it's around the corner)
Nice to have
• Follow us on Facebook
Follow us on twitter
Services we offer
Should not have
• Should not have too bright colors that people won't be able to see in the sun.
Font should not be old-style fonts.

```html
<!DOCTYPE html>
<html lang="en">
<head>
<meta charset="utf-8">
<title>Lesedi Day Spa – Street Sign</title>
<link rel="stylesheet" href="https://fonts.googleapis.com/css2?family=Carlito:ital,wght@0,400;0,700;1,400&display=swap">
<style>
  :root {
    --paper: #ffffff;
    --fern-lime: #c7da2c;
    --fern-lime-soft: #d9e66a;
    --fern-sky: #a9d3ee;
    --brand-green: #8cc63f;
    --tagline-grey: #a6a6a6;
    --text-dark: #3a3a3a;
    --social-blue: #3b5b97;
    --social-sky: #4fb3e3;
  }
  * { margin: 0; padding: 0; box-sizing: border-box; }
  html, body { width: 1200px; height: 599px; overflow: hidden; background: var(--paper); }
  .sign {
    position: relative;
    width: 1200px;
    height: 599px;
    background: var(--paper);
    font-family: "Carlito", "Calibri", sans-serif;
    color: var(--text-dark);
    overflow: hidden;
  }
  .foliage { position: absolute; inset: 0; width: 1200px; height: 599px; }
  .brand-name {
    position: absolute;
    left: 20px;
    top: 212px;
    font-size: 78px;
    font-weight: 400;
    line-height: 1;
    color: var(--brand-green);
    letter-spacing: -0.5px;
  }
  .tagline {
    position: absolute;
    left: 64px;
    top: 302px;
    font-size: 37px;
    font-style: italic;
    color: var(--tagline-grey);
    line-height: 1;
  }
  .contact-line {
    position: absolute;
    font-size: 28px;
    line-height: 1;
    white-space: nowrap;
  }
  .contact-phone { left: 54px; top: 396px; }
  .contact-follow { left: 606px; top: 396px; }
  .contact-web { left: 113px; top: 456px; }
  .contact-address { left: 181px; top: 526px; }
  .social-square {
    position: absolute;
    top: 390px;
    width: 46px;
    height: 46px;
    border-radius: 7px;
  }
  .social-square.first { left: 834px; background: var(--social-blue); }
  .social-square.second { left: 898px; background: var(--social-sky); }
</style>
</head>
<body>
  <main class="sign">
    <svg class="foliage" viewBox="0 0 1200 599" aria-hidden="false">
      <defs>
        <linearGradient id="limeFade" x1="0" y1="0" x2="1" y2="1">
          <stop offset="0" stop-color="var(--fern-lime)"/>
          <stop offset="1" stop-color="var(--fern-lime-soft)"/>
        </linearGradient>
        <linearGradient id="skyFade" x1="0" y1="0" x2="1" y2="0">
          <stop offset="0" stop-color="#c8e4f5"/>
          <stop offset="1" stop-color="var(--fern-sky)"/>
        </linearGradient>
      </defs>
      <path role="img" aria-label="Light blue fern frond decoration"
            fill="url(#skyFade)"
            d="M70 0 L360 0 C345 70 290 110 210 80 C150 55 110 30 70 0 Z"/>
      <path role="img" aria-label="Large lime green fern fronds decoration"
            fill="url(#limeFade)"
            d="M440 0 L1200 0 L1200 400 C1080 360 960 300 860 230 C760 170 660 120 560 80 C500 55 460 25 440 0 Z"/>
      <path role="img" aria-label="Long lime green fern leaf decoration"
            fill="url(#limeFade)"
            d="M60 168 C260 150 470 120 640 100 C720 92 780 96 820 110 C700 128 520 150 330 168 C220 178 130 180 60 168 Z"/>
      <path role="img" aria-label="Lime green fern fronds decoration"
            fill="url(#limeFade)"
            d="M460 599 C600 540 760 470 920 430 C1030 405 1120 400 1200 405 L1200 599 Z"/>
    </svg>

    <h1 class="brand-name">Lesedi Day Spa</h1>
    <p class="tagline">Beauty . Health .Slimming</p>

    <p class="contact-line contact-phone">TEL:011 742 3198/011 657 4031</p>
    <p class="contact-line contact-follow">Follow us on:</p>
    <span class="social-square first"></span>
    <span class="social-square second"></span>
    <p class="contact-line contact-web">www.lesedidayspa.example.za</p>
    <p class="contact-line contact-address">23 Kestrel Road</p>
  </main>
</body>
</html>
```